Zero Tax Seminar Postcard Design

I need a postcard designed that is 5.5" x 8.5". Color front and back with space for an address block and postal indicia. I will provide the bullet points and copy. I need assistance with the layout, organization and perhaps a couple of images, etc. This postcard will drive individuals to a web site to register for a 90-minute seminar teaching them how to minimize or eliminate their income taxes during retirement.
Target Market(s)
Married Couples, ages 50 - 70. Successful and affluent. People that appreciate and value professional advice and relationships.
Requirements
Must have
- Bright and Bold.  Compelling and attention grabbing.
Call to action #1 - Go to website immediately for further information.
Call to action #2 - Call the office immediately to register.

```html
<!DOCTYPE html>
<html lang="en">
<head>
<meta charset="utf-8">
<title>The Zero Tax Solution – Seminar Postcard</title>
<link href="https://fonts.googleapis.com/css2?family=Lato:wght@400;700&family=Oswald:wght@400&display=swap" rel="stylesheet">
<style>
  :root {
    --stage: #1e1a1a;
    --paper: #ffffff;
    --ink: #555555;
    --ink-dark: #222222;
    --accent: #f6a023;
    --link: #8e1b1b;
    --rule: #9a9a9a;
    --photo-a: #d9a94a;
    --photo-b: #8a9a3a;
    --photo-c: #c9b48a;
  }
  * { box-sizing: border-box; margin: 0; padding: 0; }
  html, body { width: 1200px; height: 1100px; overflow: hidden; }
  body { background: var(--stage); position: relative; font-family: "Lato", Arial, sans-serif; color: var(--ink); }

  .card { position: absolute; background: var(--paper); }
  .card--back { left: 163px; top: 10px; width: 823px; height: 532px; }
  .card--front { left: 163px; top: 552px; width: 825px; height: 533px; overflow: hidden; }

  /* back */
  .message { position: absolute; left: 20px; width: 384px; top: 76px; text-align: center; font-size: 16px; line-height: 20px; }
  .message h2 { font-size: 18px; font-weight: 400; color: var(--ink-dark); margin-bottom: 20px; }
  .message p { margin-bottom: 20px; }
  .message .accent { color: var(--link); }
  .divider { position: absolute; left: 428px; top: 66px; width: 1px; height: 409px; background: var(--rule); }
  .stamp { position: absolute; left: 699px; top: 62px; width: 83px; height: 83px; border: 1px solid var(--rule); }
  .address-line { position: absolute; left: 462px; width: 325px; height: 1px; background: var(--rule); }

  /* front */
  .hero-photo { position: absolute; left: 0; top: 0; width: 383px; height: 256px;
    background: radial-gradient(ellipse at 60% 55%, var(--photo-c) 0%, var(--photo-a) 45%, var(--photo-b) 100%); }
  .hero-panel { position: absolute; left: 383px; top: 0; width: 442px; height: 256px; background: var(--accent); color: var(--paper); text-align: center; }
  .hero-title { font-family: "Oswald", "Arial Narrow", sans-serif; font-weight: 400; font-size: 38px; line-height: 44px; margin-top: 40px; }
  .hero-sub { font-size: 16px; line-height: 20px; margin: 20px 30px 0; }

  .points { position: absolute; left: 24px; top: 270px; width: 740px; list-style: none; }
  .point { position: relative; padding-left: 41px; font-size: 15.5px; line-height: 20px; margin-bottom: 12px; }
  .point svg { position: absolute; left: 0; top: 2px; width: 24px; height: 24px; }
  .bottom-band { position: absolute; left: 0; bottom: 0; width: 100%; height: 5px; background: var(--accent); }
</style>
</head>
<body>

<section class="card card--back">
  <div class="message">
    <h2>Register Today!!</h2>
    <p>Visit <span class="accent">www.HarlanReedWealthGroup.Com</span><br>right away to learn about upcoming dates,<br>times and locations</p>
    <p>Call our office to register immediately<br><span class="accent">(555) 214-7390</span></p>
    <p>“I personally guarantee – when you attend this seminar, your view of the complex world of Wealth and Taxation will be dramatically different”</p>
    <p>More Knowledge, Increased Confidence and More Capability</p>
  </div>
  <div class="divider"></div>
  <div class="stamp"></div>
  <div class="address-line" style="top:234px"></div>
  <div class="address-line" style="top:261px"></div>
  <div class="address-line" style="top:287px"></div>
  <div class="address-line" style="top:314px"></div>
  <div class="address-line" style="top:340px"></div>
</section>

<section class="card card--front">
  <div class="hero-photo" role="img" aria-label="Smiling retired couple embracing outdoors among autumn leaves"></div>
  <div class="hero-panel">
    <h1 class="hero-title">The Zero Tax Solution<br>A Free Educational Seminar</h1>
    <p class="hero-sub">A Unique, One-Of-A-Kind Program Reveals Little Known Secrets Used By America’s Wealthiest Families To Reduce And Even Eliminate Their Income Taxes During Their Retirement Years</p>
  </div>

  <ul class="points">
    <li class="point">
      <svg viewBox="0 0 24 24"><circle cx="12" cy="12" r="11" fill="var(--accent)"/><text x="12" y="17" text-anchor="middle" font-family="Lato, sans-serif" font-weight="700" font-size="15" fill="#fff">?</text></svg>
      Are you upset or angry at the government for confiscating more and more of your hard earned money??
    </li>
    <li class="point">
      <svg viewBox="0 0 24 24"><circle cx="12" cy="12" r="11" fill="var(--accent)"/><g fill="#fff"><rect x="7" y="11" width="2" height="6"/><rect x="10" y="8" width="2" height="9"/><rect x="13" y="10" width="2" height="7"/><rect x="16" y="9" width="1.5" height="8"/></g></svg>
      Many financial experts agree that income taxes need to double (that’s right, double!!) in the next ten years or else we will fly head over heels into another financial disaster??
    </li>
    <li class="point">
      <svg viewBox="0 0 24 24"><circle cx="12" cy="12" r="11" fill="var(--accent)"/><circle cx="12" cy="11" r="3.5" fill="#fff"/><rect x="10.5" y="14" width="3" height="3" fill="#fff"/><g stroke="#fff" stroke-width="1.2"><line x1="12" y1="4.5" x2="12" y2="6"/><line x1="6" y1="11" x2="7.5" y2="11"/><line x1="16.5" y1="11" x2="18" y2="11"/><line x1="7.7" y1="6.7" x2="8.7" y2="7.7"/><line x1="16.3" y1="6.7" x2="15.3" y2="7.7"/></g></svg>
      How would you like to dramatically decrease or even eliminate your income taxes during your retirement years?? (It is possible!!)
    </li>
    <li class="point">
      <svg viewBox="0 0 24 24"><circle cx="12" cy="12" r="11" fill="var(--accent)"/><circle cx="12" cy="7.5" r="1.5" fill="#fff"/><rect x="10.8" y="10" width="2.4" height="8" fill="#fff"/></svg>
      This information is critical to your retirement plan!! Reducing or eliminating income taxes during retirement can make your financial nest egg last much longer and since Americans are living longer than ever before, you should be doing everything possible to learn about this critically important subject.
    </li>
  </ul>
  <div class="bottom-band"></div>
</section>

</body>
</html>
```